Stonefield Partners - Web Design

I have recently established a business called Stonefield Partners. The business is focused on providing property developers with project financing solutions. This is not a real estate website so please do not provide such pics or design. I provide financial solutions.

I have been in the financial markets for the past 20 years covering all asset classes from trading through to portfolio management, structuring and business development. The majority of this time was spent with building new business and expanding into new opportunities.

This is a start-up business so there isn't much content at this stage. Therefore, its all about first impressions. I want a design that portray confidence; and that I can deliver a workable solution. It must provide the perception of sophistication, innovation, yet simplistic so its not trying to deceive/hide something. Most importantly it must give the Client a sense of trust and reliability.

I would like to have the website portray my depth of experience in providing financing solutions and consultancy services in achieving the investment objectives. However, I would like to avoid looking like a one man band. I do have access to resources just not directly employed by the company.

Anyway, I hope this is enough to at least wet your appetite. I recently had a logo created on ArtHive that should set the theme/style of the website

Project Deadline Extended
Reason: Increase time to allow web designer/developer more time to understand the style I am after.

All, Thank you for your current designs. I am based in Singapore, however, I am currently traveling today but will respond by later tonight or tomorrow. Rolf

All, A general observation. Please do not include photos of houses, architectural drawings or images that portal construction or real estate. This implies I am either a property agent or in some way directly involve in selling property...very misleading. Remember, I am involved in provide financial solutions not selling property. Rolf

All, Please avoid using numerous people within the site as it may represent that my business has a large number of staff when in fact its only me. However, I also don't want to look like a "one man band". So be balanced on using people - I am not sure I want people at all. Thanks Rolf

Some designers are not reading the brief or previous messages. If you do more then once I will simply not comment and eliminate ask not to provide any more.

please stop using pictures and/or logos that imply - I manage their money - I protect their money - I grow their money - I offer homes loans - that I do house calls with individuals (i.e no couples shaking heads with a guy) - no house pictures or symbols i.e. it looks like a property website - I have a large organisation (i.e. team of people) If any design include the above I will eliminate it REMEMBER: I am providing innovative financial solutions - NOT asset/fund manager, bank manager or real estate manager thank you

All Please be creative and innovative with your pics. Also ensure you have the rights to use the pics. I have seen basic stock photos being used and again have not read by brief or previous comments. For instance, they use the words "sustainable growth" in google and click on images and you will see most of the images being used. these will be eliminated instantly and not asked to return.

Please, if you use the name of the Company as a Label or Statement can please ensure it remains in the same style as the Logo, i.e. all Caps Large with small.

All, I have decided that I don't want to have people in the main pic on the front page so please provide other inspirational pics. Thanks

guys I found a coffee advert whilst in Vietnam. I like the colour selection and thought it would be inspirational.i ahve added it yo my bried f

```html
<!DOCTYPE html>
<html lang="en">
<head>
<meta charset="utf-8">
<title>Stonefield Partners</title>
<link rel="stylesheet" href="https://fonts.googleapis.com/css2?family=Cinzel:wght@600&family=Lato:wght@400;700&family=Open+Sans:wght@300;400;600&display=swap">
<style>
:root{
  --gold:#957625;
  --gold-light:#c9a64a;
  --black:#000;
  --ink:#222;
  --text:#555;
  --muted:#777;
  --cream:#fdf8e6;
  --chip:#f1f1f1;
  --white:#fff;
  --dark-btn:#2b2b2b;
}
*{margin:0;padding:0;box-sizing:border-box}
html,body{width:1200px;height:2400px;overflow:hidden}
body{position:relative;background:var(--white);font-family:"Open Sans",Arial,sans-serif;color:var(--text)}
.abs{position:absolute}

/* hero */
.hero-visual{left:0;top:0;width:1200px;height:712px;
  background:
    radial-gradient(ellipse 190px 110px at 560px 575px,rgba(196,138,98,.95) 0%,rgba(160,102,70,.7) 45%,rgba(120,80,55,0) 100%),
    radial-gradient(ellipse 330px 230px at 90px 600px,rgba(176,166,148,.9) 0%,rgba(120,112,100,.6) 50%,rgba(60,60,60,0) 100%),
    radial-gradient(ellipse 330px 260px at 1130px 560px,rgba(120,124,130,.95) 0%,rgba(85,88,94,.65) 50%,rgba(50,50,50,0) 100%),
    radial-gradient(ellipse 120px 60px at 400px 560px,rgba(130,160,210,.55) 0%,rgba(130,160,210,0) 100%),
    radial-gradient(ellipse 430px 230px at 610px 250px,#8a8a8a 0%,#5a5a5a 40%,rgba(30,30,30,0) 100%),
    radial-gradient(ellipse 700px 420px at 600px 330px,#3a3a3a 0%,#1a1a1a 60%,#0c0c0c 100%)}
.hero-arrow{top:376px;width:32px;height:32px;border-radius:50%;background:rgba(255,255,255,.55);display:flex;align-items:center;justify-content:center}
.hero-arrow.prev{left:27px}.hero-arrow.next{left:1139px}

/* header */
.brand{left:61px;top:22px;display:flex;align-items:center;gap:12px}
.brand-mark{width:56px;height:56px;background:var(--gold)}
.brand-name{font-family:"Lato",sans-serif;font-weight:700;font-size:22px;letter-spacing:2px;color:var(--gold-light);text-transform:uppercase;line-height:1}
.phone{left:934px;top:32px;display:flex;gap:10px;align-items:center}
.phone-label{font-size:14px;color:var(--gold-light);line-height:16px}
.phone-number{font-size:24px;color:var(--white);line-height:1.1}

.main-nav{left:61px;top:110px;width:1078px;height:45px;background:var(--black);display:flex;font-family:"Lato",sans-serif;font-size:14px;color:var(--white)}
.main-nav a{color:inherit;text-decoration:none;display:flex;align-items:center;justify-content:center}
.main-nav a.active{background:var(--gold)}

/* intro band */
.intro-band{left:0;top:712px;width:1200px;height:130px;background:var(--black)}
.intro-title{left:189px;top:734px;font-family:"Cinzel",serif;font-weight:600;font-size:36px;color:var(--white);letter-spacing:1px}
.intro-text{left:189px;top:782px;width:610px;font-size:14px;line-height:19px;color:var(--white)}
.btn-start{left:806px;top:738px;width:205px;height:81px;background:var(--gold);color:var(--white);font-size:21px;line-height:24px;text-align:center;display:flex;align-items:center;justify-content:center;letter-spacing:.5px}

/* who we are */
.section-title{width:1200px;left:0;text-align:center;font-weight:300;font-size:29px;color:var(--ink)}
.who-text{left:138px;top:941px;width:924px;text-align:center;font-size:13.5px;line-height:19.5px;color:var(--text)}
.btn{height:34px;display:flex;align-items:center;justify-content:center;font-size:14.5px}
.btn-read{left:472px;top:1016px;width:110px;background:#e4e4e4;color:#555}
.btn-works{left:595px;top:1016px;width:111px;background:var(--gold);color:var(--white)}

.service{width:330px;text-align:center}
.service-visual{width:271px;height:147px;margin:0 auto}
.service-title{margin-top:19px;font-weight:600;font-size:16.5px;line-height:22px;color:var(--ink)}
.service-text{margin-top:11px;font-size:13px;line-height:18px;color:var(--muted)}

/* news */
.news-band{left:0;top:1424px;width:1200px;height:264px;background:var(--cream)}
.news-heading{left:58px;top:1444px;font-size:27px;font-weight:400;color:var(--ink)}
.news-item{top:1510px;display:flex;gap:12px}
.news-visual{width:151px;height:112px;flex:none}
.news-body{width:200px}
.news-title{font-size:15.5px;font-weight:400;color:var(--ink);line-height:20px}
.news-date{font-size:11px;color:#333;margin-top:4px}
.news-text{font-size:11px;line-height:15px;color:var(--text);margin-top:8px}
.news-more{font-size:11px;color:var(--muted);margin-top:8px;display:flex;align-items:center;gap:6px}

/* clients */
.client{top:1806px;width:176px;height:63px;background:var(--chip);display:flex;align-items:center;justify-content:center;gap:8px;font-size:20px;color:#333}
.client-dot{width:16px;height:16px;border-radius:50%;background:#333}
.clients-text{left:200px;top:1910px;width:800px;text-align:center;font-size:13px;line-height:19px;color:var(--muted)}

/* cta */
.cta-band{left:0;top:2021px;width:1200px;height:109px;background:var(--gold)}
.cta-title{left:293px;top:2048px;font-family:"Lato",sans-serif;font-weight:700;font-size:41px;color:var(--white)}
.cta-btn{left:760px;top:2051px;width:138px;height:45px;background:var(--dark-btn);color:var(--white);font-family:"Lato",sans-serif;font-weight:700;font-size:12px;letter-spacing:.5px;display:flex;align-items:center;justify-content:center}

/* footer */
.footer{left:0;top:2130px;width:1200px;height:270px;background:var(--black)}
.footer-nav a{position:absolute;top:2202px;font-size:13px;color:#8a8a8a;text-decoration:none;transform:translateX(-50%)}
.footer-rule{left:0;top:2290px;width:1200px;height:1px;background:#2a2a2a}
.to-top{left:586px;top:2280px;width:26px;height:22px;background:var(--black);display:flex;justify-content:center}
.copyright{left:61px;top:2342px;font-size:11px;color:#aaa}
.social{top:2330px;width:26px;height:26px;transform:rotate(45deg);border:1.5px solid #ddd;display:flex;align-items:center;justify-content:center}
.social span{width:6px;height:6px;background:#ddd}
.social.active{width:34px;height:34px;top:2326px;background:var(--white);border-color:var(--white)}
.social.active span{background:var(--black)}
</style>
</head>
<body>

<div class="abs hero-visual" role="img" aria-label="Two business people in suits shaking hands in front of a faint grey world map on a dark background"></div>
<div class="abs hero-arrow prev"><svg width="12" height="14" viewBox="0 0 12 14"><path d="M9 1 3 7l6 6" fill="none" stroke="#333" stroke-width="2.5"/></svg></div>
<div class="abs hero-arrow next"><svg width="12" height="14" viewBox="0 0 12 14"><path d="M3 1l6 6-6 6" fill="none" stroke="#333" stroke-width="2.5"/></svg></div>

<header>
  <div class="abs brand"><div class="brand-mark"></div><div class="brand-name">Stonefield Partners</div></div>
  <div class="abs phone">
    <svg width="18" height="32" viewBox="0 0 20 34"><path d="M6 2c-3 1-5 4-5 9 0 7 4 15 9 20 2 2 5 2 7 0l1-2-5-6-3 2c-2-3-4-8-4-12l3-1-1-8z" fill="#c9a64a"/></svg>
    <div><div class="phone-label">Call us on:</div><div class="phone-number">0845 210 7730</div></div>
  </div>
  <nav class="abs main-nav">
    <a class="active" style="width:110px">Home</a>
    <a style="width:123px">About Us</a>
    <a style="width:118px">Service</a>
    <a style="width:174px">financing solutions</a>
    <a style="width:123px">News &amp; Blog</a>
    <a style="width:112px">Clients</a>
    <a style="width:147px">Testimonials</a>
    <a style="width:171px">Contact Us</a>
  </nav>
</header>

<section>
  <div class="abs intro-band"></div>
  <div class="abs intro-title">STONEFIELD</div>
  <p class="abs intro-text">We are in the financial markets for the past 20 years covering all asset classes from trading through to portfolio management, structuring and business development.</p>
  <div class="abs btn-start">GET STARTED<br>NOW</div>
</section>

<section>
  <h2 class="abs section-title" style="top:884px">Who We Are</h2>
  <p class="abs who-text">Lorem ipsum dolor sit amet, consectetur adipiscing elit. Nunc rutrum varius mi et luctus. Donec vitae erat lorem. Quisque suscipit ultricies dui vel scelerisque. In lobortis tristique odio, eget rhoncus eros. Praesent eleifend ornare libero, sed varius ligula ultricies id. Nulla id pharetra lorem. Integer tincidunt consectetur eros et bibendum. Nam at nisl ligula.</p>
  <div class="abs btn btn-read">Read More</div>
  <div class="abs btn btn-works">View Works</div>

  <div class="abs service" style="left:61px;top:1122px">
    <div class="service-visual" role="img" aria-label="Businessman drawing a rising growth chart" style="background:linear-gradient(160deg,#c9cdd2,#8d949c 60%,#5b6168)"></div>
    <h3 class="service-title">Property developers with project<br>financing solutions</h3>
    <p class="service-text">Nunc interdum tellus vitae dui tempor, at congue nulla blandit. Nulla tincidunt ornare tellus at mollis. Integer sit amet lacus pretium.</p>
  </div>
  <div class="abs service" style="left:437px;top:1122px">
    <div class="service-visual" role="img" aria-label="Magnifying glass over an asset allocation document" style="background:linear-gradient(150deg,#f2f2f2,#cfd5dc 55%,#8fa3b8)"></div>
    <h3 class="service-title">All asset classes from trading through to<br>portfolio management</h3>
    <p class="service-text">Nunc interdum tellus vitae dui tempor, at congue nulla blandit. Nulla tincidunt ornare tellus at mollis. Integer sit amet lacus pretium.</p>
  </div>
  <div class="abs service" style="left:812px;top:1122px">
    <div class="service-visual" role="img" aria-label="Large interlocking gears under a cloudy sky" style="background:linear-gradient(180deg,#d8d6cf,#a8a59a 55%,#4a4a46)"></div>
    <h3 class="service-title">Structuring and business<br>development</h3>
    <p class="service-text">Nunc interdum tellus vitae dui tempor, at congue nulla blandit. Nulla tincidunt ornare tellus at mollis. Integer sit amet lacus pretium.</p>
  </div>
</section>

<section>
  <div class="abs news-band"></div>
  <h2 class="abs news-heading">Latest News</h2>

  <article class="abs news-item" style="left:59px">
    <div class="news-visual" role="img" aria-label="Figure lifting a barbell of coins" style="background:linear-gradient(160deg,#b9a47a,#7d6a4a 60%,#4a3f2e)"></div>
    <div class="news-body">
      <h3 class="news-title">Lorem ipsum dolor sit</h3>
      <div class="news-date">15/05/15 &nbsp; · &nbsp; Friday</div>
      <p class="news-text">Pellentesque laoreet iaculis tempor. Sed ultricies ullamcorper magna, vel tempus lacus dapibus ac.</p>
      <div class="news-more">Read More <svg width="9" height="9" viewBox="0 0 9 9"><circle cx="4.5" cy="4.5" r="4.5" fill="#999"/><path d="M3.5 2.5l2 2-2 2" stroke="#fff" fill="none"/></svg></div>
    </div>
  </article>
  <article class="abs news-item" style="left:426px">
    <div class="news-visual" role="img" aria-label="Business meeting around a bright office table" style="background:linear-gradient(160deg,#f4f4f4,#cfcfcf 60%,#8a8a8a)"></div>
    <div class="news-body">
      <h3 class="news-title">Lorem ipsum dolor sit</h3>
      <div class="news-date">15/05/15 &nbsp; · &nbsp; Friday</div>
      <p class="news-text">Pellentesque laoreet iaculis tempor. Sed ultricies ullamcorper magna, vel tempus lacus dapibus ac.</p>
      <div class="news-more">Read More <svg width="9" height="9" viewBox="0 0 9 9"><circle cx="4.5" cy="4.5" r="4.5" fill="#999"/><path d="M3.5 2.5l2 2-2 2" stroke="#fff" fill="none"/></svg></div>
    </div>
  </article>
  <article class="abs news-item" style="left:794px">
    <div class="news-visual" role="img" aria-label="Hand touching a glowing digital interface" style="background:linear-gradient(160deg,#3a4a5c,#1d2733 60%,#0c1118)"></div>
    <div class="news-body">
      <h3 class="news-title">Lorem ipsum dolor sit</h3>
      <div class="news-date">15/05/15 &nbsp; · &nbsp; Friday</div>
      <p class="news-text">Pellentesque laoreet iaculis tempor. Sed ultricies ullamcorper magna, vel tempus lacus dapibus ac.</p>
      <div class="news-more">Read More <svg width="9" height="9" viewBox="0 0 9 9"><circle cx="4.5" cy="4.5" r="4.5" fill="#999"/><path d="M3.5 2.5l2 2-2 2" stroke="#fff" fill="none"/></svg></div>
    </div>
  </article>
</section>

<section>
  <h2 class="abs section-title" style="top:1728px">Clients We’ve Worked So Far</h2>
  <div class="abs client" style="left:106px"><span class="client-dot"></span>Northline</div>
  <div class="abs client" style="left:310px"><span class="client-dot"></span>Ferncrest</div>
  <div class="abs client" style="left:514px"><span class="client-dot"></span>Quarryview</div>
  <div class="abs client" style="left:717px"><span class="client-dot"></span>Haldenway</div>
  <div class="abs client" style="left:920px"><span class="client-dot"></span>Brightwater</div>
  <p class="abs clients-text">Ut molestie ultricies quam. Donec at sem. Praesent pretium. Maorbi quis nulla vehicula felsd laoreet. Sed ullamcorper arcuSed tempus tempor cild &nbsp;Nulla vierra ultrices magnal Nam rutrum congue diam. Sed do eiusmod tempor incididunt ut labore</p>
</section>

<section>
  <div class="abs cta-band"></div>
  <h2 class="abs cta-title">Want to work with us?</h2>
  <div class="abs cta-btn">GET IN TOUCH</div>
</section>

<footer>
  <div class="abs footer"></div>
  <nav class="footer-nav">
    <a style="left:128px">Home</a>
    <a style="left:242px">About Us</a>
    <a style="left:358px">Service</a>
    <a style="left:504px">financing solutions</a>
    <a style="left:669px">News &amp; Blog</a>
    <a style="left:795px">Clients</a>
    <a style="left:921px">Testimonials</a>
    <a style="left:1061px">Contact Us</a>
  </nav>
  <div class="abs footer-rule"></div>
  <div class="abs to-top"><svg width="16" height="18" viewBox="0 0 16 18"><path d="M2 9l6-6 6 6M2 15l6-6 6 6" fill="none" stroke="#ccc" stroke-width="1.6"/></svg></div>
  <div class="abs copyright">copyrights © 2015 yoursite All rights reserved</div>
  <div class="abs social" style="left:916px"><span></span></div>
  <div class="abs social" style="left:954px"><span></span></div>
  <div class="abs social active" style="left:988px"><span></span></div>
  <div class="abs social" style="left:1030px"><span></span></div>
  <div class="abs social" style="left:1068px"><span></span></div>
  <div class="abs social" style="left:1106px"><span></span></div>
</footer>

</body>
</html>
```